Webdesign for starlight path

"Der Sternpfad" is a new info product that will be selled through the website maybe you will create for us.

Translated from german to english the project is named "the starlight path". It´s an online video course that teaches people how to live a fulfilling, happy and healthy life.

Design paramaters
We want a serious design that embodies the real feeling of beeing happy and fulfilled. Visitors should even feel good/better when they see the website.
In color psychology some sort of calming deep green like a four-leaf clover is recommend.
Mainly the website will be the external sales page with a big video as the central attention.
We also need a member area for customers to watch our video course.

So mainly we need a eye-cathing, calming header, the content body with mainly video and just a few written words...and of course a footer for links like imprint, affiliate program etc.

What we not want:
- some kind of these exaggerated smiling photos
- that bathetic luck symbols like money or boats

Hi,

i posted a message to the design discussion. Thank you!

```html
<!DOCTYPE html>
<html lang="en">
<head>
<meta charset="utf-8">
<title>the starlight path</title>
<link rel="stylesheet" href="https://fonts.googleapis.com/css2?family=Questrial&family=Ubuntu:wght@400&family=Roboto:wght@400&family=Crimson+Text&display=swap">
<style>
  :root {
    --green-deep: #0a6b2a;
    --green-mid: #2a8a2f;
    --green-lime: #8cc63f;
    --green-pale: #e9f7df;
    --ink: #333333;
    --grey: #8a8a8a;
    --amp-grey: #9a9a9a;
    --player-frame: #cfcfcf;
    --player-bg: #141414;
    --player-bar: #232323;
    --white: #ffffff;
  }
  * { margin: 0; padding: 0; box-sizing: border-box; }
  html, body { width: 1200px; height: 1093px; overflow: hidden; background: var(--white); }
  .page {
    position: relative; width: 1200px; height: 1093px; overflow: hidden;
    background:
      radial-gradient(ellipse 140px 120px at 80px 30px, var(--green-pale), transparent 70%),
      radial-gradient(ellipse 110px 110px at 1180px 40px, var(--green-pale), transparent 70%),
      var(--white);
  }
  .member-tab {
    position: absolute; left: 843px; top: 0; width: 140px; height: 32px;
    background: linear-gradient(#2e8a2e, var(--green-deep));
    border-radius: 0 0 12px 12px;
    color: var(--white); font: 14px "Ubuntu", sans-serif;
    text-align: center; padding-top: 11px;
  }
  .member-tab::before {
    content: ""; position: absolute; left: 64px; top: 5px;
    border: 5px solid transparent; border-top-color: var(--white); border-bottom: 0;
  }
  .brand {
    position: absolute; left: 207px; top: 56px; display: flex; align-items: center; gap: 12px;
    font: 35px "Questrial", sans-serif; color: var(--green-deep); letter-spacing: -0.5px;
  }
  .brand-dot { width: 18px; height: 18px; border-radius: 50%; background: var(--green-deep); }
  .main-nav {
    position: absolute; left: 600px; top: 66px; height: 39px;
    display: flex; align-items: center; font: 15px "Ubuntu", sans-serif; color: var(--ink);
  }
  .main-nav a { color: var(--ink); text-decoration: none; }
  .main-nav .active {
    background: linear-gradient(#1f8a2c, var(--green-deep)); color: var(--white);
    height: 39px; width: 76px; display: flex; align-items: center; justify-content: center;
    margin-right: 24px;
  }
  .main-nav .sep { color: var(--green-deep); margin: 2px 20px 0; }
  .hero-art {
    position: absolute; left: 0; top: 140px; width: 1200px; height: 360px;
    background:
      radial-gradient(ellipse 220px 200px at 935px 180px, rgba(140,198,63,0.28), transparent 70%),
      linear-gradient(172deg, rgba(255,255,255,0) 30%, rgba(140,198,63,0.22) 52%, rgba(10,107,42,0.28) 68%, rgba(255,255,255,0) 92%);
  }
  .hero-shade {
    position: absolute; left: 220px; top: 140px; width: 810px; height: 30px;
    background: radial-gradient(ellipse at top, rgba(0,0,0,0.07), transparent 70%);
  }
  .headline { font-family: "Questrial", sans-serif; font-weight: 400; color: var(--green-deep); }
  .headline span { position: absolute; white-space: nowrap; line-height: 1; }
  .headline .line-1 { left: 331px; top: 184px; font-size: 32px; letter-spacing: -0.8px; }
  .headline .line-2 { left: 370px; top: 212px; font-size: 60px; letter-spacing: -1.8px; }
  .headline .line-3 { left: 492px; top: 272px; font-size: 36px; letter-spacing: -1.2px; }
  .headline .amp { position: static; color: var(--amp-grey); font-size: 44px; margin: 0 2px; vertical-align: -4px; }
  .author {
    position: absolute; left: 536px; top: 322px; width: 226px; text-align: center;
    font: 15px "Crimson Text", serif; color: var(--grey);
  }
  .author::before, .author::after {
    content: ""; position: absolute; top: 11px; width: 34px; border-top: 1px dotted #b5b5b5;
  }
  .author::before { left: 0; } .author::after { right: 0; }
  .author strong { font-weight: 400; color: var(--green-deep); }
  .player {
    position: absolute; left: 236px; top: 512px; width: 729px; height: 344px;
    background: var(--player-frame); padding: 8px 8px 8px 6px;
  }
  .player-screen { position: relative; width: 100%; height: 100%; background: var(--player-bg); }
  .play-big { position: absolute; left: 244px; top: 29px; }
  .player-controls {
    position: absolute; left: 0; bottom: 0; width: 100%; height: 53px; background: var(--player-bar);
    display: flex; align-items: center; padding: 0 14px;
  }
  .ctrl { display: block; }
  .timecode { margin-left: auto; font: 9px "Roboto", sans-serif; color: #d8d8d8; letter-spacing: 0.5px; }
  .intro {
    position: absolute; left: 228px; top: 881px; width: 735px;
    font: 11px/16px "Roboto", sans-serif; color: var(--ink); letter-spacing: 0.15px;
  }
  .footer-shade {
    position: absolute; left: 200px; top: 966px; width: 830px; height: 42px;
    background: radial-gradient(ellipse at bottom, rgba(0,0,0,0.08), transparent 70%);
  }
  .footer {
    position: absolute; left: 206px; top: 1044px; width: 785px; display: flex; justify-content: space-between;
    font: 11.5px "Roboto", sans-serif; color: var(--green-deep);
  }
  .footer a { color: var(--green-deep); text-decoration: none; }
</style>
</head>
<body>
<div class="page">
  <a class="member-tab">Member Area</a>

  <div class="brand"><span class="brand-dot"></span><span>the starlight path</span></div>

  <nav class="main-nav">
    <a class="active">Home</a>
    <a>About Us</a><span class="sep">|</span>
    <a>Our Course</a><span class="sep">|</span>
    <a>Contact Us</a>
  </nav>

  <div class="hero-art" role="img" aria-label="Flowing green ribbon illustration with a large leaf motif"></div>
  <div class="hero-shade"></div>

  <h1 class="headline">
    <span class="line-1">The cosmic sources of</span>
    <span class="line-2">Self-knowledge</span>
    <span class="line-3">Love<span class="amp">&amp;</span>Partnership</span>
  </h1>
  <p class="author">Author: <strong>Lorenz Albrecht</strong></p>

  <section class="player">
    <div class="player-screen">
      <svg class="play-big" width="224" height="224" viewBox="0 0 224 224" aria-label="Play video">
        <defs>
          <radialGradient id="btn" cx="0.45" cy="0.35" r="0.7">
            <stop offset="0" stop-color="#a6e03a"/>
            <stop offset="0.7" stop-color="#6cb51e"/>
            <stop offset="1" stop-color="#4a8f14"/>
          </radialGradient>
        </defs>
        <circle cx="112" cy="112" r="111" fill="#000"/>
        <circle cx="112" cy="112" r="102" fill="url(#btn)"/>
        <path d="M75,51 L174,109 L75,167 Z" fill="#fff"/>
      </svg>
      <div class="player-controls">
        <svg class="ctrl" width="84" height="30" viewBox="0 0 84 30">
          <circle cx="8" cy="15" r="6" fill="#e5e5e5"/><path d="M5,12 v6 M11,12 L7,15 L11,18 Z" stroke="#222" stroke-width="1.4" fill="#222"/>
          <circle cx="38" cy="15" r="13" fill="#bdbdbd"/><circle cx="38" cy="15" r="10.5" fill="#1b1b1b"/><path d="M34,9 L45,15 L34,21 Z" fill="#fff"/>
          <circle cx="68" cy="15" r="6" fill="#e5e5e5"/><path d="M71,12 v6 M65,12 L69,15 L65,18 Z" stroke="#222" stroke-width="1.4" fill="#222"/>
        </svg>
        <span class="timecode">00:00 / 00:00</span>
        <svg class="ctrl" width="46" height="12" viewBox="0 0 46 12" style="margin-left:12px">
          <g fill="#a9c7f2">
            <rect x="0" y="10" width="2" height="2"/><rect x="4" y="10" width="2" height="2"/><rect x="8" y="9" width="2" height="3"/><rect x="12" y="9" width="2" height="3"/><rect x="16" y="8" width="2" height="4"/><rect x="20" y="7" width="2" height="5"/><rect x="24" y="6" width="2" height="6"/><rect x="28" y="5" width="2" height="7"/><rect x="32" y="4" width="2" height="8"/><rect x="36" y="3" width="2" height="9"/><rect x="40" y="2" width="2" height="10"/>
          </g>
        </svg>
        <svg class="ctrl" width="16" height="14" viewBox="0 0 16 14" style="margin-left:12px">
          <rect x="0.5" y="0.5" width="15" height="13" fill="#8fb6e8" stroke="#cfe0f5"/><rect x="3" y="4" width="10" height="2" fill="#fff"/><rect x="3" y="8" width="10" height="2" fill="#fff"/>
        </svg>
      </div>
    </div>
  </section>

  <p class="intro">Only a few find what they crave. We all have the power sources in order to make our fortune really. The interconnectedness of humans with the cosmos has been scientifically proven and biophysicist Lorenz Albrecht explains first how we can use the resulting energy for us. Why do we find it so difficult to be happy? Why do not we often succeed in finding the right partner and build strong relationships? The biophysicist Lorenz Albrecht break new ground in order to answer these questions. He is convinced that until we find ourselves and our desire even then partner, if we go back to the cosmic source of life. ....</p>

  <div class="footer-shade"></div>
  <footer class="footer">
    <nav><a>Home</a> - <a>About Us</a> - <a>Our Course</a> - <a>Imprint</a> - &nbsp;<a>Affiliate program</a> - <a>Contact Us</a></nav>
    <span>2012 The starlightpath.com, Inc. All rights reserved,</span>
  </footer>
</div>
</body>
</html>
```